Business Card Design

I'm a commercial general contractor remodel offices, hotels, health clubs and stores mostly San Francisco and the peninsula
the file I down loaded is kind of what I want I like the I beam with my company name in it, that would be fine with me but if you have better Idea will look at it you never know, I'm decided to give in and change my company name to how every one knows me, I have been in business since 1991, I like the I beam logo I included one of my old card from my old company for reference for you.

Industry/Entity Type

Business

Contact Information for Business Card

BRAXO CONSTRUCTION (is my company name)
Warrick Dunleavy contractor, LIc 831276
4318 Fenwick Row, San Bruno, California 94783
mobile, (415) 555-0147
phone (650) 555-0182
Fax, (650) 555-0183
email, braxo@braxoconstruction.example

```html
<!DOCTYPE html>
<html lang="en">
<head>
<meta charset="utf-8">
<title>Braxo Construction – Business Card</title>
<link rel="stylesheet" href="https://fonts.googleapis.com/css2?family=Open+Sans:wght@400;600&display=swap">
<style>
  :root {
    --backdrop: #e9e9e9;
    --card-black: #1b1b1b;
    --card-black-light: #2c2c2c;
    --accent-blue: #1b86cf;
    --text-white: #ffffff;
    --text-grey: #d2d2d2;
    --tab-edge: #e6e6e6;
  }
  html, body {
    margin: 0;
    width: 1200px;
    height: 844px;
    overflow: hidden;
    background: var(--backdrop);
    font-family: "Open Sans", sans-serif;
  }
  .canvas {
    position: relative;
    width: 1200px;
    height: 844px;
  }
  .card {
    position: absolute;
    top: 272px;
    width: 525px;
    height: 300px;
    overflow: hidden;
    box-shadow: 0 6px 18px rgba(0,0,0,0.25);
  }
  /* Contact side */
  .card-back {
    left: 50px;
    background: linear-gradient(100deg, var(--card-black) 55%, var(--card-black-light) 100%);
  }
  .band {
    position: absolute;
    left: 0;
    width: 100%;
    height: 13px;
    background: var(--accent-blue);
  }
  .band-top { top: 0; }
  .band-bottom { bottom: 0; }
  .contact {
    position: absolute;
    top: 42px;
    left: 0;
    width: 100%;
    text-align: center;
    color: var(--text-grey);
    font-size: 14px;
    line-height: 19px;
  }
  .contact-name {
    display: inline-block;
    margin: 0;
    padding: 0 6px 3px;
    font-size: 19px;
    font-weight: 600;
    letter-spacing: 0.3px;
    color: var(--text-white);
    border-bottom: 1px solid var(--accent-blue);
  }
  .contact-role {
    margin: 2px 0 0;
    color: var(--accent-blue);
  }
  .contact-license { margin: 0; }
  .contact-phones {
    list-style: none;
    margin: 22px 0 0;
    padding: 0;
  }
  .contact-email { margin: 6px 0 0; }
  .contact-address { margin: 8px 0 0; font-size: 15px; }

  /* Logo side */
  .card-front {
    left: 625px;
    background: radial-gradient(ellipse 60% 55% at 52% 40%, #3a3a3a 0%, var(--card-black) 70%);
  }
  .tab {
    position: absolute;
    width: 24px;
    height: 38px;
    background: var(--accent-blue);
    border-right: 5px solid var(--tab-edge);
  }
  .tab-top-right { top: 34px; right: 0; border-right: none; border-left: 5px solid var(--tab-edge); }
  .tab-left { top: 180px; left: 0; }
  .brand-name {
    position: absolute;
    top: 118px;
    left: 0;
    width: 100%;
    margin: 0;
    text-align: center;
    font-size: 30px;
    font-weight: 600;
    letter-spacing: 1px;
    color: var(--accent-blue);
  }
</style>
</head>
<body>
<main class="canvas">
  <section class="card card-back" aria-label="Contact side">
    <div class="band band-top"></div>
    <div class="contact">
      <h1 class="contact-name">WARRICK DUNLEAVY</h1>
      <p class="contact-role">Contractor,</p>
      <p class="contact-license">Llc 831276</p>
      <ul class="contact-phones">
        <li>(415) 555-0147</li>
        <li>(650) 555-0182</li>
        <li>(650) 555-0183</li>
      </ul>
      <p class="contact-email">braxo@braxoconstruction.example</p>
      <p class="contact-address">4318 Fenwick Row,San Bruno, California 94783</p>
    </div>
    <div class="band band-bottom"></div>
  </section>

  <section class="card card-front" aria-label="Logo side">
    <div class="tab tab-top-right"></div>
    <div class="tab tab-left"></div>
    <p class="brand-name">BRAXO CONSTRUCTION</p>
  </section>
</main>
</body>
</html>
```